Vastmere Holdings Webpage Design

We need a new website for our company. The company is Vastmere Holdings Pty Ltd. We are in the business of Asbestos Removal; Demolition; Earthworks and Transport. We do not advertise and would like our website to be a reference point for our clients / potential clients and also to make our services known to those searching the internet for the services we offer. Some examples of the style of website we are after are:
http://www.quorrintdemolition.com.au/
http://m.feltrovindemolitions.com.au/
http://www.pinsettodemolition.com.au
http://www.rulqa.com.au
http://www.tjhservices.com.au
http://www.steadfield-deconstruction.com.au
We will need to work on content. Enclosed is an example. We also need to purchase the domain vastmereholdings.com.au and need to set up email accounts and ensure the website is mobile friendly. We have a company logo and have built our business on delivering professional, quality services on time. We would like the webpage to be simple, informative and professional - black and white / grey themed. We would also like to add a photo gallery etc later.

Industry/Entity Type

Construction

Coding

Coded - Design and coding required

Number of Pages Required

1 page

Colors
000000
fcfcfc
959595
dddddd

Requirements
Must have
• Information regarding the services we provide

```html
<!DOCTYPE html>
<html lang="en">
<head>
<meta charset="utf-8">
<title>Vastmere Holdings</title>
<link href="https://fonts.googleapis.com/css2?family=Michroma&family=Arimo:wght@400;700&display=swap" rel="stylesheet">
<style>
:root{
  --black:#000000;
  --white:#fcfcfc;
  --grey:#959595;
  --light:#dddddd;
  --accent:#b5473a;
  --nav-active:#d8806e;
  --dark:#231f20;
  --button:#8a8a8a;
}
*{box-sizing:border-box;margin:0;padding:0}
html,body{width:1200px;height:3579px;overflow:hidden}
body{position:relative;background:var(--white);font-family:'Arimo',Arial,sans-serif;color:var(--white)}
.abs{position:absolute}
.display{font-family:'Michroma','Arial Black',sans-serif}
.center{text-align:center}

/* hero */
.hero{left:0;top:0;width:1200px;height:656px;background:linear-gradient(180deg,#3b3d3f 0%,#56524a 45%,#3a342c 100%)}
.nav{top:18px;left:0;width:1200px;display:flex;justify-content:center;gap:42px;font-size:22px;letter-spacing:.5px}
.nav span{color:var(--white)}
.nav .active{color:var(--nav-active)}
.brand{top:150px;left:0;width:1200px;font-size:52px;letter-spacing:6px;color:var(--white)}
.hero-service{width:240px;text-align:center;font-size:20px;letter-spacing:3px}
.hero-circle{width:114px;height:114px;border-radius:50%;border:3px solid var(--white);background:#e9e7e2;margin:0 auto}
.hero-circle.dark{background:#1b1b1b}
.dots{display:flex;gap:14px;justify-content:center;align-items:center}
.dots i{width:8px;height:8px;border-radius:50%;background:var(--accent);display:block}
.dots i.on{background:transparent;border:2px solid var(--light);width:14px;height:14px}

/* welcome */
.welcome-title{top:712px;left:0;width:1200px;font-size:37px;color:#333;letter-spacing:3px}
.welcome-title em{font-style:normal;color:var(--accent)}
.welcome-text{top:774px;left:188px;width:824px;font-size:14.5px;line-height:21px;color:#555}
.btn{display:flex;align-items:center;justify-content:center;font-family:'Michroma',sans-serif;font-size:17px;letter-spacing:3px;color:var(--white)}
.btn.grey{background:var(--button)}
.btn.black{background:var(--black)}

/* services */
.services{left:0;top:971px;width:1200px;height:551px;background:linear-gradient(135deg,#2a2a2a 0%,#45423d 50%,#2d2b28 100%)}
.person{left:0;top:943px;width:262px;height:579px;background:linear-gradient(180deg,#b8998a 0%,#8c8f93 35%,#6d7176 70%,#5a6f8c 100%);border-radius:120px 120px 0 0}
.svc-title{top:1176px;left:322px;width:310px;font-size:19px;color:var(--accent);letter-spacing:2px}
.svc-text{top:1222px;left:322px;width:310px;font-size:14px;line-height:26px;color:var(--white)}
.tile{width:197px;height:198px;border:2px solid var(--white);display:flex;flex-direction:column;align-items:center;justify-content:center;gap:22px;font-family:'Michroma',sans-serif;font-size:17px;letter-spacing:2px;text-align:center;line-height:28px}
.tile.filled{background:#1d1d1d;border-color:#1d1d1d}

/* testimonial */
.testimonial{left:0;top:1522px;width:1200px;height:482px;background:linear-gradient(180deg,#1f1f1f 0%,#3a3835 60%,#2b2a28 100%)}
.test-title{top:1578px;left:0;width:1200px;font-size:38px;letter-spacing:1px}
.avatar{left:547px;top:1640px;width:104px;height:104px;border-radius:50%;border:4px solid #ddd;background:linear-gradient(135deg,#8a5a58,#c49a8e)}
.client-name{top:1764px;left:0;width:1200px;font-size:21px;letter-spacing:3px}
.client-role{top:1802px;left:0;width:1200px;font-size:12px;letter-spacing:2px;font-family:'Michroma',sans-serif}
.quote{top:1846px;left:215px;width:770px;font-size:15px;line-height:25px;font-style:italic}

/* gallery */
.gallery-title{top:2064px;left:0;width:1200px;font-size:30px;color:#222;letter-spacing:4px}
.photo{display:block}

/* contact */
.contact{left:0;top:2806px;width:1200px;height:558px;background:linear-gradient(180deg,#233438 0%,#3b4448 55%,#4a4640 100%)}
.contact-title{top:2862px;left:0;width:1200px;font-size:34px;letter-spacing:4px}
.sub-title{font-size:19px;letter-spacing:3px;text-align:center}
.field{left:76px;width:501px;height:47px;background:var(--white);color:#888;font-size:13px;padding:14px 14px}
.field.first{border:3px solid #6fb9c8}
.submit{left:262px;top:3254px;width:134px;height:134px;border-radius:50%;background:#1e1c1c;display:flex;align-items:center;justify-content:center;font-family:'Michroma',sans-serif;font-size:21px;letter-spacing:3px;z-index:2}
.person-name{left:725px;font-size:20px}
.person-name em{font-size:17px}
.detail{left:725px;display:flex;align-items:center;gap:18px;font-size:16px;color:var(--light)}
.detail svg{width:22px;height:22px;margin-left:30px}

/* footer */
.footer{left:0;top:3364px;width:1200px;height:215px;background:var(--dark)}
.copyright{top:3538px;left:0;width:1200px;font-size:15px;color:var(--light)}
</style>
</head>
<body>

<!-- hero -->
<div class="abs hero" role="img" aria-label="Mining haul truck and excavator working on a dark quarry site"></div>
<nav class="abs nav"><span class="active">HOME</span><span>ABOUT US</span><span>SERVICES</span><span>SAFETY</span><span>ENVIRONMENT</span><span>CONTACT US</span></nav>
<div class="abs brand display center">VASTMERE HOLDINGS</div>

<div class="abs hero-service" style="left:231px;top:349px">
  <div class="hero-circle" role="img" aria-label="Dump truck icon"></div>
  <div style="margin-top:18px">TRANSPORT</div>
</div>
<div class="abs hero-service display" style="left:479px;top:337px">
  <div style="margin-bottom:16px">DEMOLITION</div>
  <div class="hero-circle dark" role="img" aria-label="Demolition excavator icon"></div>
</div>
<div class="abs hero-service display" style="left:730px;top:349px">
  <div class="hero-circle" role="img" aria-label="Earthmoving excavator icon"></div>
  <div style="margin-top:18px">EARTHMOVING</div>
</div>
<div class="abs hero-service display" style="left:231px;top:504px;display:none"></div>
<div class="abs dots" style="left:0;top:606px;width:1200px"><i class="on"></i><i></i><i></i><i></i></div>

<!-- welcome -->
<h1 class="abs welcome-title display center" style="font-weight:400">WELCOME TO THE <em>VASTMERE HOLDINGS</em></h1>
<p class="abs welcome-text center">Vastmere Transport Pty Ltd was established by Director Marcus Hellory in 2002 with a focus providing services within the transport industry. Over time the company has developed and expanded to include the provision of Earthworks and Demolition. Marcus has over 10 years' experience working at all levels within these industries focusing primarily on Demolition...</p>
<div class="abs btn grey" style="left:496px;top:866px;width:208px;height:52px">READ MORE</div>

<!-- services -->
<div class="abs services" role="img" aria-label="Dark quarry landscape backdrop"></div>
<div class="abs person" role="img" aria-label="Smiling man in a grey shirt with arms crossed"></div>
<svg class="abs" style="left:417px;top:1065px" width="120" height="100" viewBox="0 0 120 100" aria-hidden="true">
  <g fill="none" stroke="#fcfcfc" stroke-width="4" stroke-linecap="round">
    <circle cx="60" cy="55" r="22"/>
    <line x1="30" y1="20" x2="44" y2="34"/><line x1="90" y1="20" x2="76" y2="34"/>
    <line x1="60" y1="8" x2="60" y2="24"/><line x1="14" y1="55" x2="30" y2="55"/><line x1="106" y1="55" x2="90" y2="55"/>
  </g>
</svg>
<div class="abs svc-title display center">DEMOLITION</div>
<p class="abs svc-text center">Vastmere Transport and Demolition provide an extensive range of demolition services. A large amount of experience across a broad range of projects results in a dependable service and peace of mind for all clients. Services include:<br>•&nbsp;&nbsp;Commercial Demolition</p>
<div class="abs btn black" style="left:384px;top:1415px;width:189px;height:40px;font-size:15px">READ MORE</div>

<div class="abs tile filled" style="left:706px;top:1038px">
  <svg width="60" height="60" viewBox="0 0 60 60" aria-hidden="true"><g fill="none" stroke="#fcfcfc" stroke-width="4"><circle cx="30" cy="32" r="16"/><line x1="10" y1="8" x2="20" y2="18"/><line x1="50" y1="8" x2="40" y2="18"/></g></svg>
  <span>DEMOLITION</span>
</div>
<div class="abs tile" style="left:926px;top:1038px">
  <svg width="60" height="60" viewBox="0 0 60 60" aria-hidden="true"><g fill="none" stroke="#fcfcfc" stroke-width="4"><rect x="10" y="26" width="34" height="16"/><line x1="44" y1="30" x2="54" y2="16"/><circle cx="18" cy="48" r="5"/><circle cx="36" cy="48" r="5"/></g></svg>
  <span>EARTHWORKS</span>
</div>
<div class="abs tile" style="left:706px;top:1257px">
  <svg width="60" height="60" viewBox="0 0 60 60" aria-hidden="true"><g fill="none" stroke="#fcfcfc" stroke-width="4"><circle cx="30" cy="24" r="14"/><line x1="12" y1="44" x2="48" y2="56"/><line x1="48" y1="44" x2="12" y2="56"/></g></svg>
  <span>ASBESTOS</span>
</div>
<div class="abs tile" style="left:926px;top:1257px">
  <svg width="60" height="60" viewBox="0 0 60 60" aria-hidden="true"><circle cx="30" cy="30" r="24" fill="#fcfcfc"/><text x="30" y="38" text-anchor="middle" font-family="Arimo,sans-serif" font-weight="700" font-size="22" fill="#1d1d1d">24</text></svg>
  <span>HOURS OF<br>OPERATION</span>
</div>

<!-- testimonial -->
<div class="abs testimonial" role="img" aria-label="Dark wooden deck backdrop"></div>
<h2 class="abs test-title center" style="font-weight:400;font-family:'Michroma',sans-serif;font-size:32px">WHAT OUR CLIENT SAY</h2>
<div class="abs avatar" role="img" aria-label="Client portrait"></div>
<div class="abs client-name display center">NINA CALDOR</div>
<div class="abs client-role center">WRITER &amp; BLOGGER, CANDA</div>
<p class="abs quote center">"Lorem Ipsum is simply dummy text of the printing and typesetting industry. Lorem Ipsum has been the industry's standard dummy text ever since the 1500s, when an unknown printer took a galley of type and scrambled it to make a type specimen book."</p>
<div class="abs dots" style="left:0;top:1962px;width:1200px"><i class="on" style="background:var(--light);border:none;width:10px;height:10px"></i><i style="background:#555"></i><i style="background:#555"></i><i style="background:#555"></i></div>

<!-- gallery -->
<h2 class="abs gallery-title display center" style="font-weight:400">OUR GALLERY</h2>
<div class="abs photo" style="left:86px;top:2140px;width:191px;height:174px;background:linear-gradient(135deg,#c98a4a,#8e6a4c);border:8px solid #9a9a9a" role="img" aria-label="Hard hats and safety gear"></div>
<div class="abs photo" style="left:282px;top:2140px;width:357px;height:174px;background:linear-gradient(135deg,#b9a98a,#a5412f)" role="img" aria-label="Worker in red overalls laying bricks"></div>
<div class="abs photo" style="left:647px;top:2140px;width:200px;height:174px;background:linear-gradient(180deg,#4f86c0,#c8a24a)" role="img" aria-label="Tower cranes against blue sky"></div>
<div class="abs photo" style="left:854px;top:2140px;width:263px;height:174px;background:linear-gradient(180deg,#5f90c6,#a58a52)" role="img" aria-label="Yellow bulldozer on a demolition site"></div>
<div class="abs photo" style="left:86px;top:2322px;width:186px;height:162px;background:linear-gradient(135deg,#8b8074,#c9b79b)" role="img" aria-label="Truck unloading rubble"></div>
<div class="abs photo" style="left:282px;top:2322px;width:262px;height:162px;background:linear-gradient(180deg,#cfd3d6,#b59a74)" role="img" aria-label="Earthworks site with cranes"></div>
<div class="abs photo" style="left:551px;top:2322px;width:272px;height:162px;background:linear-gradient(135deg,#6f6a62,#c49a3c)" role="img" aria-label="Construction worker with hard hat"></div>
<div class="abs photo" style="left:833px;top:2322px;width:284px;height:162px;background:linear-gradient(180deg,#4f86c0,#d09a2a)" role="img" aria-label="Yellow excavator"></div>
<div class="abs photo" style="left:86px;top:2494px;width:253px;height:178px;background:linear-gradient(180deg,#9aa0a4,#5a4e44)" role="img" aria-label="Mining operation with onlookers"></div>
<div class="abs photo" style="left:346px;top:2494px;width:267px;height:178px;background:linear-gradient(135deg,#7a8a9a,#5a3a30)" role="img" aria-label="Demolished building debris"></div>
<div class="abs photo" style="left:620px;top:2494px;width:225px;height:178px;background:linear-gradient(180deg,#e6a43a,#3a2a1a)" role="img" aria-label="Crane silhouettes at sunset"></div>
<div class="abs photo" style="left:852px;top:2494px;width:265px;height:178px;background:linear-gradient(135deg,#a58a8a,#3f5a7a)" role="img" aria-label="Worker using a jackhammer"></div>
<div class="abs btn grey" style="left:496px;top:2703px;width:208px;height:50px">VIEW ALL</div>

<!-- contact -->
<div class="abs contact" role="img" aria-label="City skyline backdrop"></div>
<h2 class="abs contact-title display center" style="font-weight:400">CONTACT US</h2>
<div class="abs sub-title display" style="left:176px;top:2958px;width:300px">INQUIRY FORM</div>
<div class="abs sub-title display" style="left:690px;top:2958px;width:300px">COMPANY DETAIL</div>

<div class="abs field first" style="top:3009px">Enter Name:</div>
<div class="abs field" style="top:3071px">Enter Phone no.:</div>
<div class="abs field" style="top:3133px">Enter E-Mail:</div>
<div class="abs field" style="top:3195px;height:131px">Message:</div>
<div class="abs submit">SUBMIT</div>

<div class="abs person-name" style="top:3004px">Marcus Hellory, <em>Director</em></div>
<div class="abs detail" style="top:3052px"><svg viewBox="0 0 22 22" aria-hidden="true"><path d="M11 2a7 7 0 0 0-7 7c0 5 7 12 7 12s7-7 7-12a7 7 0 0 0-7-7z" fill="#b5473a"/><circle cx="11" cy="9" r="2.5" fill="#3b4448"/></svg>PO Box 512 KELLOWAY QLD 4311</div>
<div class="abs detail" style="top:3090px"><svg viewBox="0 0 22 22" aria-hidden="true"><rect x="2" y="5" width="18" height="13" fill="#b5473a"/><path d="M2 5l9 7 9-7" fill="none" stroke="#3b4448" stroke-width="1.5"/></svg>vhdemolition@mailbox.com</div>
<div class="abs detail" style="top:3128px"><svg viewBox="0 0 22 22" aria-hidden="true"><path d="M5 2l4 4-2 3c1 2 3 4 5 5l3-2 4 4-3 3C9 19 3 13 2 5z" fill="#b5473a"/></svg>0400 123 567</div>

<div class="abs person-name" style="top:3180px">Leah Dorran, <em>Administration</em></div>
<div class="abs detail" style="top:3233px"><svg viewBox="0 0 22 22" aria-hidden="true"><path d="M11 2a7 7 0 0 0-7 7c0 5 7 12 7 12s7-7 7-12a7 7 0 0 0-7-7z" fill="#b5473a"/><circle cx="11" cy="9" r="2.5" fill="#3b4448"/></svg>PO Box 512 KELLOWAY QLD 4311</div>
<div class="abs detail" style="top:3269px"><svg viewBox="0 0 22 22" aria-hidden="true"><rect x="2" y="5" width="18" height="13" fill="#b5473a"/><path d="M2 5l9 7 9-7" fill="none" stroke="#3b4448" stroke-width="1.5"/></svg>vhdemolition@mailbox.com</div>
<div class="abs detail" style="top:3305px"><svg viewBox="0 0 22 22" aria-hidden="true"><path d="M5 2l4 4-2 3c1 2 3 4 5 5l3-2 4 4-3 3C9 19 3 13 2 5z" fill="#b5473a"/></svg>0400 765 321</div>

<svg class="abs" style="left:587px;top:3334px" width="26" height="24" viewBox="0 0 26 24" aria-hidden="true"><g fill="none" stroke="#fcfcfc" stroke-width="3"><path d="M4 12l9-8 9 8"/><path d="M4 21l9-8 9 8"/></g></svg>

<!-- footer -->
<div class="abs footer"></div>
<svg class="abs" style="left:510px;top:3385px" width="180" height="66" viewBox="0 0 180 66" aria-hidden="true">
  <g fill="none" stroke="#fcfcfc" stroke-width="2">
    <rect x="22" y="10" width="32" height="32" transform="rotate(45 38 26) translate(0 7)"/>
    <rect x="74" y="10" width="32" height="32" transform="rotate(45 90 26) translate(0 7)"/>
    <rect x="130" y="10" width="32" height="32" transform="rotate(45 146 26) translate(0 7)"/>
  </g>
  <rect x="24" y="19" width="28" height="28" transform="rotate(45 38 33)" fill="#fcfcfc"/>
</svg>
<div class="abs copyright center">© VASTMERE HOLDINGS - 2015. All rights reserved.</div>

</body>
</html>
```